Velisto Events Business Card

We need a business cards that stands out to our clients. We are company who targets prestige clients to spend money with us on experiences, so our image needs to be prestige
Target Market(s)
Corporate
Contact Information for Business Card
There will be four different names on the business cards
Dana Morrowby
Director
O: 02 5147 3086
M: 0451 692 038
E: info@velistoevents.example.au
Facebook: @velistoevents
Instagram: velistoevents
www.velistoevents.example.au
Nathaniel Morrowby
Director
O: 02 5147 3086
M: 0467 215 904
Facebook: @velistoevents
Instagram: velistoevents
www.velistoevents.example.au
Teodor Vinkel
Director
O: 02 5147 3086
M: 0478 903 527
Facebook: @velistoevents
Instagram: velistoevents
www.velistoevents.example.au
Mabel Hartung
Director
O: 02 5147 3086
Facebook: @velistoevents
Instagram: velistoevents
www.velistoevents.example.au
Colors
Designer to choose colors to be used in the design.
Look and feel

```html
<!DOCTYPE html>
<html lang="en">
<head>
<meta charset="utf-8">
<title>Velisto Events Business Card</title>
<link rel="stylesheet" href="https://fonts.googleapis.com/css2?family=Cinzel:wght@500&family=Libre+Baskerville:wght@400;700&display=swap">
<style>
  :root {
    --backdrop: #e4e4e6;
    --paper: #f1f0f2;
    --navy: #272352;
    --ink: #3a3366;
    --text: #2b2b33;
    --gold-light: #f6e2a0;
    --gold: #d9a840;
    --gold-deep: #b98a2c;
    --gold-text: #d8ad52;
  }
  * { box-sizing: border-box; margin: 0; padding: 0; }
  html, body {
    width: 1200px;
    height: 1000px;
    overflow: hidden;
    background: var(--backdrop);
  }
  .canvas {
    position: relative;
    width: 1200px;
    height: 1000px;
  }
  .card {
    position: absolute;
    width: 516px;
    height: 296px;
  }

  /* Front: contact side */
  .card-front {
    left: 349px;
    top: 189px;
    background: var(--paper);
  }
  .brand-mark {
    position: absolute;
    left: 40px;
    top: 50px;
    width: 190px;
    height: 196px;
    display: flex;
    align-items: center;
    justify-content: center;
    font-family: "Cinzel", serif;
    font-weight: 500;
    font-size: 23px;
    letter-spacing: 2px;
    color: var(--ink);
    text-align: center;
  }
  .contact-block {
    position: absolute;
    left: 268px;
    top: 86px;
    font-family: "Libre Baskerville", serif;
    color: var(--text);
  }
  .person-name {
    font-weight: 700;
    font-size: 17px;
    letter-spacing: 0.4px;
    color: var(--ink);
    text-transform: uppercase;
    line-height: 22px;
  }
  .person-role {
    font-size: 15px;
    line-height: 22px;
  }
  .contact-list {
    list-style: none;
    margin-top: 40px;
  }
  .contact-list li {
    display: flex;
    align-items: center;
    font-size: 14px;
    line-height: 22px;
  }
  .contact-list svg {
    width: 16px;
    height: 14px;
    margin-right: 9px;
    fill: var(--ink);
    flex: none;
  }

  /* Back: brand side */
  .card-back {
    left: 346px;
    top: 531px;
    background: linear-gradient(115deg, var(--gold) 0%, var(--gold-light) 22%, var(--gold) 45%, var(--gold-deep) 62%, var(--gold-light) 82%, var(--gold) 100%);
    padding: 19px 19px 20px 19px;
  }
  .card-back-field {
    width: 100%;
    height: 100%;
    background: radial-gradient(ellipse at 50% 30%, #34305f 0%, var(--navy) 70%);
    display: flex;
    align-items: center;
    justify-content: center;
  }
  .brand-name {
    font-family: "Cinzel", serif;
    font-weight: 500;
    font-size: 30px;
    letter-spacing: 6px;
    color: var(--gold-text);
    text-transform: uppercase;
  }
</style>
</head>
<body>
<main class="canvas">
  <section class="card card-front" aria-label="Business card front">
    <div class="brand-mark">Velisto Events</div>
    <div class="contact-block">
      <p class="person-name">Elias Marlowe</p>
      <p class="person-role">Director</p>
      <ul class="contact-list">
        <li>
          <svg viewBox="0 0 16 14" aria-hidden="true"><path d="M1 4.5C1 2 3 1 8 1s7 1 7 3.5v1h-3.2V4H4.2v1.5H1zM4 6.5h8l2.5 6.5h-13z"/><circle cx="8" cy="9.6" r="1.8" fill="#f1f0f2"/></svg>
          012 345 6789
        </li>
        <li>
          <svg viewBox="0 0 16 14" aria-hidden="true"><path d="M1 2h14v1.6L8 8 1 3.6z"/><path d="M1 5.2l7 4.4 7-4.4V12H1z"/></svg>
          hello@velisto.example
        </li>
        <li>
          <svg viewBox="0 0 16 16" aria-hidden="true" fill="none" stroke="#3a3366" stroke-width="1.4" style="fill:none"><circle cx="8" cy="8" r="6.5"/><ellipse cx="8" cy="8" rx="2.8" ry="6.5"/><path d="M1.5 8h13M2.6 4.6h10.8M2.6 11.4h10.8"/></svg>
          www.velisto.example
        </li>
      </ul>
    </div>
  </section>

  <section class="card card-back" aria-label="Business card back">
    <div class="card-back-field">
      <p class="brand-name">Velisto Events</p>
    </div>
  </section>
</main>
</body>
</html>
```